Banner ads for VL that work with same theme as below banners

Love the banner ads below. Need more with attached photos. But use the same wording, font as in below banner ads. Should be VL size 1200/627 so I can use for Trovique and VL. Looking for great ads to use as VL ads. We do lots of ads so it will be worth your time to enter this contest you will be rewarded with a ton of work. Need several banner ads that work together. So maybe 1 of the dresses, 1 of the sweater, 1 of the leggings, 1 of the jacket

Target Market(s)

Women 24-45

Industry/Entity Type

Fashion

Requirements
Must have
• Banner ads that work for VL and Trovique
Nice to have
• Several options to choose from
Should not have
• not sure

```html
<!DOCTYPE html>
<html lang="en">
<head>
<meta charset="utf-8">
<title>Season Collections – Banner Set</title>
<link rel="stylesheet" href="https://fonts.googleapis.com/css2?family=Kaushan+Script&family=Lilita+One&family=Roboto+Slab:wght@300;900&display=swap">
<style>
  :root {
    --page: #ffffff;
    --legging-bg: #b3b3bb;
    --stone-bg: #ececec;
    --sky-bg: #d0ebf6;
    --ink: #222222;
    --navy-script: #3b3f6b;
    --blue: #1aa3e8;
    --brick: #b03a32;
    --line: #333333;
    --frame: #8a8a8a;
    --chip: #ffffff;
  }
  * { margin: 0; padding: 0; box-sizing: border-box; }
  html, body { width: 1200px; height: 1200px; overflow: hidden; background: var(--page); }
  .banner-set { position: absolute; left: 313px; top: 0; width: 575px; height: 1200px; }
  .banner { position: relative; width: 575px; height: 300px; overflow: hidden; }
  .banner--leggings { background: var(--legging-bg); }
  .banner--dress { background: radial-gradient(circle at 40% 50%, #f4f4f4, var(--stone-bg) 70%, #e2e2e2); }
  .banner--jacket { background: var(--sky-bg); }
  .banner--sweater { background: var(--sky-bg); }
  .deco { position: absolute; inset: 0; width: 575px; height: 300px; }
  .photo { position: absolute; }
  .script, .headline { position: absolute; transform: translateX(-50%); white-space: nowrap; }
  .script { font-family: "Kaushan Script", cursive; line-height: 1; }
  .headline { font-family: "Lilita One", sans-serif; line-height: 1; letter-spacing: 0.5px; }
  .cta {
    position: absolute; white-space: nowrap;
    background: var(--chip); color: var(--ink);
    font-family: "Roboto Slab", serif; text-align: center; letter-spacing: 1.6px;
    display: flex; align-items: center; justify-content: center; gap: 0.35em;
  }
  .cta b { font-weight: 900; }
  .cta span { font-weight: 300; }
</style>
</head>
<body>
<main class="banner-set">

  <section class="banner banner--leggings">
    <svg class="deco" viewBox="0 0 719 375" preserveAspectRatio="none">
      <g fill="none" stroke="var(--line)" stroke-width="2">
        <line x1="64" y1="200" x2="259" y2="8"/>
        <polygon points="141,135 334,-58 527,135 334,328"/>
        <line x1="404" y1="268" x2="597" y2="78"/>
        <line x1="594" y1="375" x2="719" y2="258"/>
        <line x1="612" y1="375" x2="719" y2="275"/>
      </g>
    </svg>
    <div class="photo" role="img" aria-label="Model's legs in navy leggings with white lace print" style="left:199px;top:0;width:120px;height:268px;background:linear-gradient(180deg,#2b2f4a,#1e2138 70%,#d8c2b4);"></div>
    <div class="script" style="left:457px;top:136px;font-size:30px;color:var(--navy-script);">leggings</div>
    <div class="headline" style="left:457px;top:179px;font-size:24px;color:#ffffff;">COLLECTION</div>
    <div class="cta" style="left:385px;top:216px;width:145px;height:22px;font-size:11px;"><b>SHOP</b><span>THE</span><b>SEASON</b></div>
  </section>

  <section class="banner banner--dress">
    <svg class="deco" viewBox="0 0 719 375" preserveAspectRatio="none">
      <rect x="245" y="42" width="444" height="288" fill="none" stroke="var(--frame)" stroke-width="4"/>
    </svg>
    <div class="photo" role="img" aria-label="Model in a black lace handkerchief-hem dress" style="left:199px;top:16px;width:80px;height:254px;background:linear-gradient(180deg,#a0785a 0%,#1b1b1b 15%,#141414 90%,#2a2a2a);"></div>
    <div class="script" style="left:415px;top:82px;font-size:30px;color:var(--ink);">Night Lace</div>
    <div class="headline" style="left:415px;top:118px;font-size:24px;color:var(--blue);">COLLECTION</div>
    <div class="cta" style="left:345px;top:175px;width:145px;height:22px;font-size:11px;background:var(--blue);color:#ffffff;"><b>SHOP</b><span>THE</span><b>SEASON</b></div>
  </section>

  <section class="banner banner--jacket">
    <div class="photo" role="img" aria-label="Model in a navy puffer jacket with fur hood in a snowy landscape" style="left:0;top:0;width:575px;height:300px;background:linear-gradient(180deg,#8ea8bc 0%,#c3d6e2 40%,#e0f3fa 60%,#e0f3fa 100%);"></div>
    <div class="photo" role="img" aria-label="Navy puffer jacket" style="left:152px;top:150px;width:210px;height:150px;background:linear-gradient(180deg,#2f4261,#1f2d47);border-radius:60px 60px 0 0;"></div>
    <svg class="deco" viewBox="0 0 719 375" preserveAspectRatio="none">
      <g fill="none" stroke="var(--line)" stroke-width="2">
        <polyline points="520,66 437,150 495,182"/>
        <polyline points="534,66 451,150 509,182"/>
        <line x1="674" y1="182" x2="536" y2="309"/>
        <line x1="652" y1="207" x2="582" y2="274"/>
      </g>
    </svg>
    <div class="script" style="left:440px;top:99px;font-size:17px;color:var(--blue);">Winter Wear</div>
    <div class="headline" style="left:440px;top:122px;font-size:15px;color:var(--ink);">COLLECTION</div>
    <div class="cta" style="left:384px;top:155px;width:111px;height:17px;font-size:8.5px;letter-spacing:1.2px;"><b>SHOP</b><span>THE</span><b>SEASON</b></div>
  </section>

  <section class="banner banner--sweater">
    <div class="photo" role="img" aria-label="Model in a rust lace-up knit sweater dress" style="left:147px;top:37px;width:124px;height:263px;background:linear-gradient(180deg,#5a3a2a 0%,#b85142 22%,#b04a3c 90%,#c9a08a);"></div>
    <svg class="deco" viewBox="0 0 719 375" preserveAspectRatio="none">
      <g fill="none" stroke="#555555" stroke-width="2">
        <polygon points="402,167 530,40 658,167 530,294"/>
        <polygon points="421,167 549,40 677,167 549,294"/>
      </g>
    </svg>
    <div class="script" style="left:440px;top:100px;font-size:17px;color:var(--brick);">Winter Wear</div>
    <div class="headline" style="left:440px;top:122px;font-size:15px;color:var(--ink);">COLLECTION</div>
    <div class="cta" style="left:384px;top:142px;width:111px;height:17px;font-size:8.5px;letter-spacing:1.2px;"><b>SHOP</b><span>THE</span><b>SEASON</b></div>
  </section>

</main>
</body>
</html>
```